Brookfarrow Osteopathy and dry needling business card

Business card for Brookfarrow Osteopathy and Dry Needling.

Industry/Entity Type

Health

Contact Information for Business Card

I do not have a phone number yet. I also do not have an email address yet. The physical address is: 48 Lower Crane Street Brookfarrow The website is: www.brookfarrowosteosteopathy.example My details are: Dr Martin Pellowe, Osteopath (B.Clin.Sci (Ost) M.Ost BSC ECON (Hons)

Colors
0094D4
00A9DD
6FCCEA
C7EBF8
E9F6FB

Requirements
Must have
• logo on the back
Nice to have
• Maybe a space for me to write an appointment time and date on the card.

```html
<!DOCTYPE html>
<html lang="en">
<head>
<meta charset="utf-8">
<title>Brookfarrow Osteopathy and Dry Needling – Business Card</title>
<link rel="stylesheet" href="https://fonts.googleapis.com/css2?family=Poppins:wght@400;500;600;700&display=swap">
<style>
  :root {
    --blue: #0094D4;
    --blue-bright: #00A9DD;
    --blue-soft: #6FCCEA;
    --orange: #F7941D;
    --white: #FFFFFF;
    --rule: #8C8C8C;
    --backdrop: #E9F6FB;
  }
  * { box-sizing: border-box; margin: 0; padding: 0; }
  html, body { width: 1200px; height: 1200px; overflow: hidden; }
  body {
    background: var(--backdrop);
    font-family: "Poppins", sans-serif;
    display: flex; flex-direction: column; align-items: center; justify-content: center;
    gap: 56px;
  }
  .card {
    position: relative; width: 880px; height: 500px; overflow: hidden;
    box-shadow: 0 10px 30px rgba(0, 60, 90, 0.18);
  }
  .card-shapes { position: absolute; inset: 0; }
  .brand-mark {
    position: absolute; display: flex; align-items: center; justify-content: center;
    text-align: center; font-weight: 600; font-size: 19px; line-height: 1.3;
  }

  /* Back: appointment card */
  .card-back { background: var(--blue); }
  .card-back .brand-mark { left: 55px; top: 120px; width: 240px; height: 240px; color: var(--white); }
  .appointment { position: absolute; left: 400px; top: 160px; right: 40px; color: var(--blue); }
  .appointment-title { font-size: 32px; font-weight: 500; letter-spacing: 1px; margin-bottom: 28px; }
  .appointment-row { display: flex; align-items: flex-end; font-size: 18px; margin-bottom: 26px; }
  .appointment-row .label { width: 70px; }
  .appointment-row .blank { border-bottom: 1.5px solid var(--rule); height: 1px; margin: 0 10px 6px; }
  .blank-date { width: 170px; }
  .blank-time { width: 140px; }
  .meridiem { font-size: 17px; line-height: 0.95; }

  /* Front: contact card */
  .card-front { background: var(--white); }
  .card-front .brand-mark { left: 75px; top: 105px; width: 230px; height: 230px; color: var(--blue); }
  .contact { position: absolute; left: 330px; top: 200px; color: var(--white); }
  .contact-name { font-size: 34px; font-weight: 700; letter-spacing: 1px; line-height: 1.1; }
  .contact-role { font-size: 18px; margin-bottom: 14px; }
  .contact-list { list-style: none; font-size: 20px; line-height: 1.55; }
  .contact-list li { display: flex; align-items: center; gap: 10px; }
  .contact-icon { width: 26px; height: 26px; flex: none; }
  .contact-web {
    position: absolute; right: 50px; bottom: 30px;
    color: var(--blue); font-size: 24px;
  }
</style>
</head>
<body>

<section class="card card-back" aria-label="Appointment side">
  <svg class="card-shapes" viewBox="0 0 880 500" aria-hidden="true">
    <rect x="170" y="130" width="710" height="240" fill="var(--white)"/>
    <circle cx="175" cy="240" r="150" fill="var(--blue)"/>
    <circle cx="175" cy="240" r="122" fill="none" stroke="var(--white)" stroke-width="3"/>
  </svg>
  <div class="brand-mark">Brookfarrow<br>Osteopathy and<br>Dry Needling</div>
  <div class="appointment">
    <h2 class="appointment-title">Next Appoinment On</h2>
    <div class="appointment-row">
      <span class="label">Date</span><span class="blank blank-date"></span>
      <span>AT</span><span class="blank blank-time"></span>
      <span class="meridiem">am.<br>pm.</span>
    </div>
    <div class="appointment-row">
      <span class="label">Date</span><span class="blank blank-date"></span>
      <span>AT</span><span class="blank blank-time"></span>
      <span class="meridiem">am.<br>pm.</span>
    </div>
  </div>
</section>

<section class="card card-front" aria-label="Contact side">
  <svg class="card-shapes" viewBox="0 0 880 500" aria-hidden="true">
    <rect x="190" y="175" width="690" height="215" fill="var(--blue)"/>
    <circle cx="202" cy="232" r="148" fill="var(--blue)"/>
    <circle cx="190" cy="220" r="136" fill="var(--white)"/>
    <circle cx="190" cy="220" r="118" fill="none" stroke="var(--blue)" stroke-width="3"/>
  </svg>
  <div class="brand-mark">Brookfarrow<br>Osteopathy and<br>Dry Needling</div>
  <div class="contact">
    <h1 class="contact-name">DR MARTIN PELLOWE</h1>
    <p class="contact-role">Osteopath (B.Clin.Sci (Ost) M.Ost BSC ECON (Hons)</p>
    <ul class="contact-list">
      <li>
        <svg class="contact-icon" viewBox="0 0 26 26" aria-hidden="true">
          <circle cx="13" cy="13" r="13" fill="var(--orange)"/>
          <path d="M9 7c1-1 2 0 2.5 1.5s-.5 2-1 2.3c.6 1.7 2 3.2 3.6 3.9.4-.5 1-1.4 2.4-.8s2 1.6 1 2.6c-2 2-5.5.5-7.8-2.2S7 8.8 9 7z" fill="var(--white)"/>
        </svg>
        000-555-0147
      </li>
      <li>
        <svg class="contact-icon" viewBox="0 0 26 26" aria-hidden="true">
          <circle cx="13" cy="13" r="13" fill="var(--orange)"/>
          <rect x="6.5" y="8.5" width="13" height="9" fill="none" stroke="var(--white)" stroke-width="1.6"/>
          <path d="M6.5 8.5l6.5 5 6.5-5" fill="none" stroke="var(--white)" stroke-width="1.6"/>
        </svg>
        info@brookfarrow.example
      </li>
      <li>
        <svg class="contact-icon" viewBox="0 0 26 26" aria-hidden="true">
          <circle cx="13" cy="13" r="13" fill="var(--orange)"/>
          <path d="M13 20s-5-5-5-8.5a5 5 0 0 1 10 0C18 15 13 20 13 20z" fill="none" stroke="var(--white)" stroke-width="1.6"/>
          <circle cx="13" cy="11.5" r="1.8" fill="var(--white)"/>
        </svg>
        48 Lower Crane Street, Brookfarrow
      </li>
    </ul>
  </div>
  <p class="contact-web">www.brookfarrowosteosteopathy.example</p>
</section>

</body>
</html>
```